Business card design needed

Brenlo First Aid Training is a training provider in the Canberra region. We provide both public and private course bookings.

I want my business card to be fun/interesting. I have attached my own logo, however whatever you think works best will work for me.

Please see my website for more inspiration at www.brenlo-example.com.au

I would like a double sided design, and round corners please.

Some really good designs so far, just not quite the right one yet. 
Please look at my website for inspiration. 
Www.brenlo-example.com.au

Industry/Entity Type

Training

Contact Information for Business Card

Brenlo First Aid Training, Tobin Marsh, 0498563027, tobinmarsh4@mailvex-example.com.au, www.brenlo-example.com.au

```html
<!DOCTYPE html>
<html lang="en">
<head>
<meta charset="utf-8">
<title>Brenlo First Aid Training – Business Card</title>
<link rel="stylesheet" href="https://fonts.googleapis.com/css2?family=Questrial&family=Oswald:wght@600&display=swap">
<style>
  :root {
    --page: #ecebe8;
    --red: #b51f24;
    --red-light: #c9272b;
    --red-dark: #9a1a1e;
    --blue: #2b2f80;
    --blue-dark: #22266b;
    --stripe: #e6e6e6;
    --white: #ffffff;
    --text-light: #d7d8e6;
    --divider: #8a8db8;
  }
  * { box-sizing: border-box; margin: 0; padding: 0; }
  html, body { width: 1200px; height: 900px; overflow: hidden; background: var(--page); }
  .canvas { position: relative; width: 1200px; height: 900px; }

  .card {
    position: absolute;
    left: 260px;
    width: 680px;
    height: 388px;
    border-radius: 24px;
    overflow: hidden;
    box-shadow: 0 10px 28px rgba(0,0,0,.22);
    font-family: "Questrial", sans-serif;
  }
  .card--front { top: 46px; }
  .card--back { top: 466px; }
  .card__bg { position: absolute; inset: 0; width: 100%; height: 100%; }

  .brand {
    position: absolute;
    display: flex;
    align-items: center;
    gap: 12px;
    color: var(--white);
    font-family: "Questrial", sans-serif;
    font-size: 24px;
    line-height: 1.15;
  }
  .brand__dot { width: 26px; height: 26px; border-radius: 50%; background: var(--white); flex: none; }
  .card--front .brand { left: 70px; top: 160px; width: 260px; }
  .card--back .brand { left: 90px; top: 92px; width: 250px; font-size: 22px; }

  .mascot {
    position: absolute;
    background: linear-gradient(180deg, #e9c9a8 0%, #f4f4f4 45%, #2b2f80 100%);
    border-radius: 14px;
    opacity: .9;
  }
  .card--front .mascot { left: 545px; top: 92px; width: 84px; height: 120px; }
  .card--back .mascot { left: 470px; top: 28px; width: 105px; height: 170px; }

  .sign {
    position: absolute;
    background: var(--white);
    color: var(--blue);
    font-family: "Oswald", sans-serif;
    font-weight: 600;
    text-align: center;
    line-height: 1.2;
    box-shadow: 0 2px 4px rgba(0,0,0,.25);
  }
  .sign em { font-style: normal; color: var(--red); }
  .sign--slogan { left: 472px; top: 40px; width: 170px; padding: 6px 8px; font-size: 14px; transform: rotate(-6deg); }
  .sign--contact { left: 566px; top: 96px; width: 76px; padding: 6px 4px; font-size: 15px; color: var(--red); transform: rotate(-8deg); }

  .holder-name {
    position: absolute;
    left: 54px;
    top: 318px;
    color: var(--text-light);
    font-size: 24px;
  }
  .contact {
    position: absolute;
    left: 400px;
    top: 258px;
    padding-left: 18px;
    border-left: 1px solid var(--divider);
    list-style: none;
    color: var(--text-light);
    font-size: 14px;
  }
  .contact li { display: flex; align-items: center; gap: 10px; height: 34px; }
  .contact svg { width: 13px; height: 13px; flex: none; fill: var(--red-light); }
  .contact .at { color: var(--red-light); font-size: 14px; width: 13px; text-align: center; }
</style>
</head>
<body>
<main class="canvas">

  <section class="card card--front" aria-label="Card front">
    <svg class="card__bg" viewBox="0 0 680 388" preserveAspectRatio="none" aria-hidden="true">
      <defs>
        <radialGradient id="redGlowFront" cx="55%" cy="40%" r="70%">
          <stop offset="0" stop-color="#c9272b"/>
          <stop offset="1" stop-color="#9a1a1e"/>
        </radialGradient>
      </defs>
      <rect width="680" height="388" fill="url(#redGlowFront)"/>
      <polygon points="225,388 680,196 680,214 262,388" fill="#e6e6e6"/>
      <polygon points="262,388 680,214 680,388" fill="#2b2f80"/>
    </svg>
    <div class="brand"><span class="brand__dot"></span><span>Brenlo First Aid Training</span></div>
    <div class="mascot" role="img" aria-label="Cartoon trainer mascot holding up a sign"></div>
    <div class="sign sign--slogan">Canberra's <em>BEST</em> for<br>First Aid &amp; CPR Training!</div>
  </section>

  <section class="card card--back" aria-label="Card back">
    <svg class="card__bg" viewBox="0 0 680 388" preserveAspectRatio="none" aria-hidden="true">
      <defs>
        <radialGradient id="redGlowBack" cx="60%" cy="30%" r="75%">
          <stop offset="0" stop-color="#c9272b"/>
          <stop offset="1" stop-color="#9a1a1e"/>
        </radialGradient>
      </defs>
      <rect width="680" height="388" fill="url(#redGlowBack)"/>
      <polygon points="0,212 680,170 680,188 0,232" fill="#e6e6e6"/>
      <polygon points="0,232 680,188 680,388 0,388" fill="#2b2f80"/>
    </svg>
    <div class="brand"><span class="brand__dot"></span><span>Brenlo First Aid Training</span></div>
    <div class="mascot" role="img" aria-label="Cartoon trainer mascot sitting on the stripe"></div>
    <div class="sign sign--contact">Contact<br>Us!</div>

    <ul class="contact">
      <li>
        <svg viewBox="0 0 24 24" aria-hidden="true"><path d="M6.6 10.8a15 15 0 0 0 6.6 6.6l2.2-2.2c.3-.3.7-.4 1-.2 1.1.4 2.3.6 3.6.6.6 0 1 .4 1 1V20c0 .6-.4 1-1 1A17 17 0 0 1 3 4c0-.6.4-1 1-1h3.5c.6 0 1 .4 1 1 0 1.3.2 2.5.6 3.6.1.3 0 .7-.2 1z"/></svg>
        <span>0498563027</span>
      </li>
      <li><span class="at">@</span><span>tobinmarsh4@mailvex-example.com.au</span></li>
      <li>
        <svg viewBox="0 0 24 24" aria-hidden="true"><path d="M12 3 2 12h3v8h5v-6h4v6h5v-8h3z"/></svg>
        <span>www.brenlo-example.com.au</span>
      </li>
    </ul>

    <p class="holder-name">Tobin Marsh</p>
  </section>

</main>
</body>
</html>
```